Full page ad for Pinewick Queer Cinema Showcase Program

I need an ad for a program booklet for the Harrowmere Screen Festival see link:http://www.bellqueststage.example/films/festivals/hqcs
Full page: 7.25"w x 10.5"d (final trim size). I have a sample of a previous ad. If you can create a new professional yet provocative ad that would be what I want. Short deadline June 25th to submit final "We’d like to have all finished ads in house by June 25."
Thank you,
Dale Voss
Updates

https://www.wrl.example/for-wrl-professionals/marketing-toolkit/how-to-use-the-wrl-marks

Target Market(s)

successful professionals LGBT market

Industry/Entity Type

Financial Planning

Requirements
Nice to have
• let's try to have some samples of photos with "people of color"
• looking for fresh look on design

```html
<!DOCTYPE html>
<html lang="en">
<head>
<meta charset="utf-8">
<title>Harlow Financial – Full Page Ad</title>
<link rel="stylesheet" href="https://fonts.googleapis.com/css2?family=Arimo:wght@400;700&family=Dancing+Script:wght@700&display=swap">
<style>
  :root {
    --canvas-bg: #dedede;
    --page-bg: #e9e9ea;
    --royal: #2b2f9b;
    --violet: #7a2e8f;
    --ink: #111111;
    --crimson: #b0173f;
    --tab-blue: #4b57e0;
    --navy-deep: #1f1d7a;
    --navy-light: #3434b0;
    --white: #ffffff;
    --muted: #333333;
  }
  * { box-sizing: border-box; margin: 0; padding: 0; }
  html, body {
    width: 1000px; height: 1200px; overflow: hidden;
    background: var(--canvas-bg);
    font-family: "Arimo", Arial, sans-serif;
  }
  .ad {
    position: absolute; left: 100px; top: 21px;
    width: 800px; height: 1157px;
    background: linear-gradient(180deg, #ececec 0%, var(--page-bg) 60%, #e4e4e6 100%);
    overflow: hidden;
  }
  .hero-image {
    position: absolute; left: 420px; top: 0; width: 380px; height: 790px;
    background:
      linear-gradient(160deg, rgba(255,255,255,0) 40%, rgba(233,233,234,0.9) 100%),
      linear-gradient(200deg, #3b3fa8 0%, #c84a9c 18%, #9a9a9a 30%, #e84a5f 44%, #f2c43b 56%, #7cc36a 66%, #3fb3e0 76%, #6a4aa8 88%, #8b8b8b 100%);
    border-bottom-left-radius: 60% 30%;
  }
  .headline { position: absolute; left: 44px; top: 96px; color: var(--royal); font-weight: 700; line-height: 1; }
  .headline .line-1, .headline .line-2 { display: block; font-size: 68px; letter-spacing: -0.5px; }
  .headline .line-2 { margin-top: 2px; }
  .headline .line-3 { display: block; font-size: 40px; color: var(--violet); margin-top: 8px; }
  .tagline { position: absolute; left: 93px; top: 432px; }
  .tagline .lead { display: block; font-size: 34px; font-weight: 700; color: var(--ink); }
  .tagline .script {
    display: block; margin-left: -34px; margin-top: 0;
    font-family: "Dancing Script", cursive; font-size: 70px; color: var(--crimson); line-height: 1;
  }
  .service-tab {
    position: absolute; left: 0; top: 752px; width: 686px; height: 50px;
    background: var(--tab-blue); border-top-right-radius: 14px;
    color: var(--white); font-weight: 700; font-size: 27px;
    padding: 10px 0 0 44px;
  }
  .service-panel {
    position: absolute; left: 0; top: 801px; width: 800px; height: 202px;
    background: linear-gradient(90deg, var(--navy-deep) 0%, var(--navy-light) 100%);
  }
  .advisor-photo {
    position: absolute; left: 46px; top: 844px; width: 147px; height: 202px;
    background: linear-gradient(180deg, #8d8f96 0%, #b89a86 45%, #2a2b33 100%);
    border: 1px solid #bbb;
  }
  .services { position: absolute; left: 242px; top: 832px; color: var(--white); font-size: 16px; line-height: 23px; }
  .services .group-title { font-weight: 700; margin-top: 19px; }
  .services ul { list-style: none; margin-left: 4px; line-height: 21.5px; }
  .services li svg { width: 12px; height: 11px; margin-right: 8px; vertical-align: 0; }
  .contact { position: absolute; left: 318px; top: 1014px; color: var(--ink); }
  .contact .phone-web { font-size: 22px; font-weight: 700; }
  .contact .address { font-size: 17px; margin-top: 6px; color: #222; }
  .advisor-caption { position: absolute; left: 46px; top: 1060px; color: var(--ink); line-height: 1.1; }
  .advisor-caption .name { font-size: 13px; }
  .advisor-caption .name sup { font-size: 9px; }
  .advisor-caption .title { font-size: 10.5px; color: var(--muted); }
  .disclaimer { position: absolute; left: 46px; top: 1126px; font-size: 11px; color: #222; }
  .brand { position: absolute; left: 580px; top: 1098px; display: flex; align-items: center; gap: 10px; color: var(--royal); font-size: 22px; font-weight: 400; letter-spacing: 1px; }
  .brand .brand-square { width: 22px; height: 22px; background: var(--royal); }
</style>
</head>
<body>
  <main class="ad">
    <div class="hero-image" role="img" aria-label="Portrait of a man in glasses overlaid with rainbow paint strokes"></div>

    <h1 class="headline">
      <span class="line-1">Successful</span>
      <span class="line-2">gay male</span>
      <span class="line-3">seeks partner...</span>
    </h1>

    <p class="tagline">
      <span class="lead">to keep me on a sound</span>
      <span class="script">financial track.</span>
    </p>

    <div class="service-tab">Concierge level service for the LGBT community</div>
    <section class="service-panel"></section>

    <div class="advisor-photo" role="img" aria-label="Headshot of advisor Dale Voss"></div>

    <div class="services">
      <p>Investments • Retirement Plan Rollovers • Estate Conservation</p>
      <p>Retirement and Financial Planning</p>
      <p class="group-title">Portfolio Review and Asset Management</p>
      <ul>
        <li><svg viewBox="0 0 12 11"><polyline points="1,6 4.5,9.5 11,1" fill="none" stroke="#fff" stroke-width="1.8"/></svg>Low-cost</li>
        <li><svg viewBox="0 0 12 11"><polyline points="1,6 4.5,9.5 11,1" fill="none" stroke="#fff" stroke-width="1.8"/></svg>Commission-free</li>
        <li><svg viewBox="0 0 12 11"><polyline points="1,6 4.5,9.5 11,1" fill="none" stroke="#fff" stroke-width="1.8"/></svg>Fee based advisory services</li>
      </ul>
    </div>

    <div class="contact">
      <p class="phone-web">919-555-0182 · HarlowFinancial.example</p>
      <p class="address">48 Quarry Glen Lane | Ellbrook, NC 27999</p>
    </div>

    <div class="advisor-caption">
      <p class="name">Dale Voss, WRL<sup>®</sup></p>
      <p class="title">certified wealth planner™</p>
    </div>

    <p class="disclaimer">Advisory services offered through Harlow Advisors LLC, a Registered Investment Advisor firm.</p>

    <div class="brand"><span class="brand-square"></span><span>HARLOW FINANCIAL</span></div>
  </main>
</body>
</html>
```